Slider needed for Database Documentation Topic

We need a slider to promote a content area of a web site. I'm listing this as a poster because the posters I have seen on FrameHarbor portfolios most closely resemble the combination or art and text I am looking for.
The content area we are promoting with this graphic will clarify the design and use of a complicated database. The title of the content area is "The Kindled VQ Database" and the banner should use that title.
To 'illuminate' something means to cast light on it, and this content area will help shed light on a complicated thing – the content will use diagrams, text, and examples to clarify the database. Another meaning is that an illuminated manuscript is a manuscript brought to life with pictures, and in a way that is also what this content area will do.
One idea for the slider might be a light bulb, lamp, candle or flashlight lighting up the words "VQ Database". Another idea would be the type of illustration you see if you search for "Illuminated manuscript"
But I'm not committed to any particular idea - in the past I have been pleased to see ideas that are different than my own but accomplish the same thing, so please feel free to use your judgement or ask any questions.
In addition to the title (The Kindled VQ Database) the graphic should allow room for three smaller lines of text – the three bullet items below:
- Guide to understanding the VQ database
- Data sources, uses and relationships explained with illustrations
- New content! Customers
The last bullet item will change as the content is added.
Some particulars ...
SIZE - 600 high x 1200 wide pixels
PHOTOS vs ILLUSTRATION - I am open to either one.

```html
<!DOCTYPE html>
<html lang="en">
<head>
<meta charset="utf-8">
<title>The Kindled VQ Database</title>
<link rel="stylesheet" href="https://fonts.googleapis.com/css2?family=IM+Fell+English+SC&family=Almendra:wght@400;700&display=swap">
<style>
  :root {
    --parchment-light: #f1dca0;
    --parchment-mid: #e6c47e;
    --parchment-dark: #c99a52;
    --border-gold: #d7ad5e;
    --border-deep: #9c6a2c;
    --title-red: #8a1414;
    --ink: #2a1608;
    --cloud-red: #b8302b;
    --server-silver: #b9bcc0;
    --server-shadow: #7d8186;
  }
  * { box-sizing: border-box; margin: 0; padding: 0; }
  html, body { width: 1200px; height: 600px; overflow: hidden; background: #ffffff; }
  .slider {
    position: relative;
    width: 1200px;
    height: 600px;
    overflow: hidden;
    background: radial-gradient(ellipse at 45% 45%, var(--parchment-light) 0%, var(--parchment-mid) 60%, var(--parchment-dark) 100%);
  }
  .frame-band {
    position: absolute;
    background: linear-gradient(180deg, var(--border-gold), var(--border-deep) 50%, var(--border-gold));
  }
  .frame-band.top { left: 0; top: 0; width: 1200px; height: 64px; }
  .frame-band.bottom { left: 0; bottom: 0; width: 1200px; height: 64px; }
  .frame-band.left { left: 0; top: 64px; width: 60px; height: 472px;
    background: linear-gradient(90deg, var(--border-gold), var(--border-deep) 50%, var(--border-gold)); }
  .frame-band.right { right: 0; top: 64px; width: 60px; height: 472px;
    background: linear-gradient(90deg, var(--border-gold), var(--border-deep) 50%, var(--border-gold)); }

  .title {
    position: absolute;
    left: 82px;
    top: 128px;
    font-family: "IM Fell English SC", serif;
    color: var(--title-red);
    line-height: 1;
  }
  .title .drop-cap {
    position: absolute;
    left: 0;
    top: 0;
    font-size: 168px;
    line-height: 1;
  }
  .title .line-one {
    position: absolute;
    left: 138px;
    top: 18px;
    font-size: 52px;
    letter-spacing: 2px;
    white-space: nowrap;
  }
  .title .line-two {
    position: absolute;
    left: 120px;
    top: 66px;
    font-size: 78px;
    letter-spacing: 4px;
    white-space: nowrap;
  }

  .bullets {
    position: absolute;
    left: 120px;
    top: 290px;
    list-style: none;
    font-family: "Almendra", serif;
    font-weight: 700;
    color: var(--ink);
    font-size: 30px;
    line-height: 36px;
  }
  .bullets li { margin-bottom: 22px; letter-spacing: 1px; }

  .cloud-art {
    position: absolute;
    left: 800px;
    top: 150px;
    width: 345px;
    height: 210px;
    border-radius: 110px 110px 30px 30px;
    background: radial-gradient(ellipse at 60% 40%, var(--cloud-red), #8e201c);
  }
  .server-art {
    position: absolute;
    left: 865px;
    top: 385px;
    width: 185px;
    height: 100px;
    border-radius: 20px;
    background: linear-gradient(180deg, var(--server-silver), var(--server-shadow));
  }
</style>
</head>
<body>
  <main class="slider">
    <div class="frame-band top" role="img" aria-label="Ornamental illuminated border band"></div>
    <div class="frame-band bottom" role="img" aria-label="Ornamental illuminated border band"></div>
    <div class="frame-band left" role="img" aria-label="Ornamental illuminated border band"></div>
    <div class="frame-band right" role="img" aria-label="Ornamental illuminated border band"></div>

    <h1 class="title">
      <span class="drop-cap">V</span>
      <span class="line-one">THE KINDLED</span>
      <span class="line-two">Q DATABASE</span>
    </h1>

    <ul class="bullets">
      <li>Guide to understanding the VQ Database</li>
      <li>Data sources, uses and relationships<br>explained with illustrations</li>
      <li>New content! Customers</li>
    </ul>

    <div class="cloud-art" role="img" aria-label="Red cloud with data bars connected to a smaller network cloud"></div>
    <div class="server-art" role="img" aria-label="Stack of silver database server cylinders"></div>
  </main>
</body>
</html>
```